Original business card of a small accounting firm

My firm specializes in accounting and taxes for small businesses. I'm looking for an original and creative business card as a marketing tool to give to prospective clients; however since we are a professional firm the card must also appear professional. I'm uploading a few examples of what I believe may fit my needs. Please feel free to use them as a jumping off point. Lastly, I'm uploading the company logo which I'd like to be the focal point on the back of the card and somewhat incorporated on the front on a smaller scale. I hope my description was helpful.
Target Market(s)
Tax clients and small businesses
Industry/Entity Type
Accounting
Contact Information for Business Card
Leonard Whitcombe
Certified Public Accountant │President
Kestrel Advisors
T│ (555) 418-2763
Email│LWhitcombe@KestrelAdvisors.example

```html
<!DOCTYPE html>
<html lang="en">
<head>
<meta charset="utf-8">
<title>Kestrel Advisors – Business Card Front</title>
<link href="https://fonts.googleapis.com/css2?family=Exo+2:wght@500;600&family=Open+Sans:wght@300;400&display=swap" rel="stylesheet">
<style>
  :root {
    --backdrop: #e9e9eb;
    --card: #fbfbfb;
    --ink: #3a3a3a;
    --ink-soft: #6b6b6b;
    --brand-blue: #3f7fc8;
    --name-blue: #43a3df;
    --band-blue: #4b84cf;
    --band-blue-deep: #3a6fb8;
    --band-grey: #6e6e72;
  }
  * { margin: 0; padding: 0; box-sizing: border-box; }
  html, body {
    width: 1200px; height: 1000px; overflow: hidden;
    background: var(--backdrop);
  }
  .card {
    position: absolute; left: 75px; top: 200px;
    width: 1050px; height: 600px;
    background: var(--card);
    box-shadow: 0 8px 30px rgba(0,0,0,0.15);
    overflow: hidden;
  }
  .edge-band {
    position: absolute; top: 0; right: 0; height: 100%;
    display: flex;
  }
  .edge-band__grey { width: 12px; background: var(--band-grey); }
  .edge-band__blue {
    width: 48px;
    background: linear-gradient(90deg, var(--band-blue), var(--band-blue-deep));
  }
  .brand {
    position: absolute; left: 150px; top: 120px;
    display: flex; flex-direction: column; gap: 8px;
  }
  .brand__row { display: flex; align-items: center; gap: 16px; }
  .brand__mark {
    width: 34px; height: 34px; background: var(--brand-blue);
  }
  .brand__name {
    font-family: "Exo 2", sans-serif; font-weight: 600;
    font-size: 46px; color: var(--ink-soft); letter-spacing: 0.5px;
  }
  .brand__tagline {
    font-family: "Open Sans", sans-serif; font-weight: 300;
    font-size: 13px; letter-spacing: 3.2px; text-transform: uppercase;
    color: var(--ink-soft); padding-left: 50px;
  }
  .person {
    position: absolute; left: 110px; top: 410px;
  }
  .person__name {
    font-family: "Exo 2", sans-serif; font-weight: 500;
    font-size: 34px; color: var(--name-blue);
  }
  .person__role {
    font-family: "Open Sans", sans-serif; font-weight: 300;
    font-size: 24px; color: var(--ink-soft); margin-top: 8px;
  }
  .person__role + .person__role { margin-top: 18px; }
  .contact {
    position: absolute; left: 560px; top: 290px;
    list-style: none;
    font-family: "Open Sans", sans-serif; font-weight: 400;
    font-size: 21px; color: var(--ink);
  }
  .contact__item { display: flex; align-items: center; gap: 14px; margin-bottom: 18px; }
  .contact__icon { width: 22px; height: 22px; flex: none; }
</style>
</head>
<body>
  <main class="card">
    <div class="brand">
      <div class="brand__row">
        <span class="brand__mark"></span>
        <span class="brand__name">Kestrel Advisors</span>
      </div>
      <span class="brand__tagline">Small Business Accounting and Taxes</span>
    </div>

    <div class="person">
      <p class="person__name">Leonard Whitcombe</p>
      <p class="person__role">President</p>
      <p class="person__role">Certified Public Accountant</p>
    </div>

    <ul class="contact">
      <li class="contact__item">
        <svg class="contact__icon" viewBox="0 0 24 24" aria-hidden="true">
          <path d="M6.6 10.8a15 15 0 0 0 6.6 6.6l2.2-2.2a1 1 0 0 1 1-.25 11.4 11.4 0 0 0 3.6.57 1 1 0 0 1 1 1V20a1 1 0 0 1-1 1A17 17 0 0 1 3 4a1 1 0 0 1 1-1h3.5a1 1 0 0 1 1 1c0 1.25.2 2.45.57 3.57a1 1 0 0 1-.25 1z" fill="#3f7fc8"/>
        </svg>
        <span>(555) 418-2763</span>
      </li>
      <li class="contact__item">
        <svg class="contact__icon" viewBox="0 0 24 24" aria-hidden="true">
          <rect x="2" y="5" width="20" height="14" rx="1.5" fill="#3f7fc8"/>
          <path d="M3 6l9 7 9-7" fill="none" stroke="#fff" stroke-width="1.6"/>
        </svg>
        <span>LWhitcombe@KestrelAdvisors.example</span>
      </li>
      <li class="contact__item">
        <svg class="contact__icon" viewBox="0 0 24 24" aria-hidden="true">
          <g fill="none" stroke="#3f7fc8" stroke-width="2.4" stroke-linecap="round">
            <path d="M10 14a4 4 0 0 0 5.6 0l3.2-3.2a4 4 0 0 0-5.6-5.6l-1.2 1.2"/>
            <path d="M14 10a4 4 0 0 0-5.6 0l-3.2 3.2a4 4 0 0 0 5.6 5.6l1.2-1.2"/>
          </g>
        </svg>
        <span>www.KestrelAdvisors.example</span>
      </li>
    </ul>

    <div class="edge-band">
      <span class="edge-band__grey"></span>
      <span class="edge-band__blue"></span>
    </div>
  </main>
</body>
</html>
```